Modern Label Design for Fruity Drink (300ml PET)

Dear Graphic Designers,

JOB BRIEF
We are a beverage manufacturer in South Africa seeking a creative wrap-around label design for our exciting new fruity drink range called Zindavo. Although our beverage doesn't contain real fruit, it's crafted to emulate the taste and appearance of authentic fruit juices, complete with essential benefits like vitamins and minerals that are contained in real fruit. Despite being priced competitively, we want the design to exude a premium feel likened to luxury juices and drinks.

TARGET MARKET
The design must possess a modern appeal that resonates with both children and adults.

DESIGN GUIDELINES
- Modern and Elegant
- Colourful
- Evokes a sense of fruit without direct explicit fruit depictions

MANDATORY ELEMENTS
1. Flavoured Drink: Law states that "Flavoured Drink" needs to be written on the front of the label, potentially integrated with the flavor name, e.g., "Orange Flavoured Drink."
2. No Fruit Images: Avoid using real fruit images, opting instead for textures and shapes that very slightly allude to the essence of fruit flavour. This is also a legal constraint.
3. Toucan Mascot: Consider incorporating a toucan or parrot as a potential mascot.
4. Logo: We have a logo, you may use this and adapt it, or design your own.
5. Claims: We need a claim on the front "High in Vitamin C, B and Zinc"

DESIGN INSPIRATION AND WARNING
Avoid drawing inspiration from our initial design attempt, shared in the files section. This design is deemed unsuitable as it appears too busy, has an 'old school' vibe, and may be perceived as exclusively for children. We aspire for a premium design that caters to adults while still being colourful.

FLAVORS
"Orange Dazzle" or alternatively "Orange Flavoured Drink"
"Berry Whirl" or alternatively "Berry Flavoured Drink"
"Tropical Lagoon" or alternatively "Tropical Flavoured Drink"
"Apple Meadow" or alternatively "Apple Flavoured Drink"

We encourage your innovative designs. Thank you for your participation, and we look forward to witnessing your creative brilliance!

Best regards,
The Marketing Team

Target Market(s)

Adults and Children (Premium)

Industry/Entity Type

Beverages

Colors

Designer to choose colors to be used in the design.

Requirements
Must have
• Premium and Colourful
Nice to have
• It would be nice to have a new or updated logo (but we have existing logo if needed), and it would be nice to have a parrot or toucan mascot somewhere
Should not have
• Looking too much like a children's fruity drink. Shouldn't contain real images or illustrations of fruit (only vaguely resembling the fruit through shapes and textures)

```html
<!DOCTYPE html>
<html lang="en">
<head>
<meta charset="utf-8">
<title>Zindavo Orange Flavoured Drink – Front Label</title>
<link rel="stylesheet" href="https://fonts.googleapis.com/css2?family=Poppins:wght@500;700;800&family=Oswald:wght@400&display=swap">
<style>
  :root {
    --label-orange: #ef8321;
    --zest-yellow: #ffe600;
    --soft-yellow: #ffd21a;
    --paper-white: #ffffff;
    --ink-dark: #1d1d1b;
  }
  * { box-sizing: border-box; margin: 0; padding: 0; }
  html, body {
    width: 857px;
    height: 1200px;
    overflow: hidden;
    background: var(--paper-white);
  }
  .canvas {
    position: relative;
    width: 857px;
    height: 1200px;
  }
  .label {
    position: absolute;
    left: 40px;
    top: 396px;
    width: 777px;
    height: 407px;
    background: var(--label-orange);
    overflow: hidden;
    font-family: "Poppins", sans-serif;
  }
  .slice-pattern {
    position: absolute;
    border-radius: 50%;
    background: radial-gradient(circle, rgba(255, 230, 0, 0.55) 0%, rgba(255, 210, 26, 0.25) 70%, rgba(239, 131, 33, 0) 100%);
  }
  .slice-pattern--top-left { left: -40px; top: -50px; width: 260px; height: 260px; }
  .slice-pattern--top-right { left: 620px; top: -40px; width: 190px; height: 170px; }
  .slice-pattern--right { left: 598px; top: 180px; width: 230px; height: 250px; }
  .slice-pattern--bottom { left: 222px; top: 336px; width: 190px; height: 140px; }
  .mascot {
    position: absolute;
    left: 494px;
    top: 85px;
    width: 140px;
    height: 146px;
    border-radius: 50%;
    background: radial-gradient(circle at 50% 40%, var(--zest-yellow) 0%, var(--soft-yellow) 60%, rgba(255, 210, 26, 0.4) 100%);
  }
  .brand-name {
    position: absolute;
    left: 180px;
    top: 100px;
    width: 440px;
    text-align: center;
    font-weight: 800;
    font-size: 96px;
    line-height: 1;
    color: var(--paper-white);
    letter-spacing: -1px;
  }
  .claim-badge {
    position: absolute;
    left: 38px;
    top: 194px;
    width: 114px;
    height: 114px;
    border-radius: 50%;
    background: var(--paper-white);
    color: var(--ink-dark);
    display: flex;
    flex-direction: column;
    align-items: center;
    justify-content: center;
    font-weight: 500;
    font-size: 17px;
    line-height: 1.2;
    text-align: center;
  }
  .volume {
    position: absolute;
    left: 36px;
    top: 336px;
    font-weight: 500;
    font-size: 32px;
    color: var(--paper-white);
  }
  .flavour-name {
    position: absolute;
    left: 180px;
    top: 282px;
    font-weight: 700;
    font-size: 46px;
    letter-spacing: 2px;
    color: var(--zest-yellow);
    transform: rotate(-9deg);
    transform-origin: left bottom;
  }
  .legal-name {
    position: absolute;
    left: 400px;
    top: 236px;
    font-family: "Oswald", sans-serif;
    font-weight: 400;
    font-size: 46px;
    line-height: 1.05;
    color: var(--paper-white);
    transform: rotate(-9deg);
    transform-origin: left top;
  }
  .legal-name span { display: block; }
  .legal-name span + span { padding-left: 8px; }
</style>
</head>
<body>
  <main class="canvas">
    <section class="label">
      <div class="slice-pattern slice-pattern--top-left" role="img" aria-label="Decorative citrus slice pattern"></div>
      <div class="slice-pattern slice-pattern--top-right" role="img" aria-label="Decorative citrus slice pattern"></div>
      <div class="slice-pattern slice-pattern--right" role="img" aria-label="Decorative citrus slice pattern"></div>
      <div class="slice-pattern slice-pattern--bottom" role="img" aria-label="Decorative citrus slice pattern"></div>
      <div class="mascot" role="img" aria-label="Yellow toucan mascot illustration"></div>

      <h1 class="brand-name">Zindavo</h1>

      <div class="claim-badge">
        <span>high in</span>
        <span>VITAMIN</span>
        <span>C,B,Zn</span>
      </div>
      <p class="volume">300 ml</p>

      <p class="flavour-name">ORANGE</p>
      <p class="legal-name"><span>FLAVOURED</span><span>DRINK</span></p>
    </section>
  </main>
</body>
</html>
```